Logo & Visitenkarte für Buchhaltung und Personal-Management
Zielgruppe
Buchhaltung und Personal- Management für KMUs
Aufgabenstellung
Schrift: Raleway sans-serif (gleich wie Text auf Homepage)
Aktuelle Logo's angefügt müssen aber überarbeitet werden.
Text für Visitenkarte:
Name: Beatrix Vonlanthen
Titel: Fachfrau für Finanz- und Rechnungswesen mit eidg. Fachausweis
Strasse: Kornacker 17
PLZ/Ort: 6099 Mattwil
Telefon: 041 675 42 09
Mail: beatrix.vonlanthen@zahlenhort-beispiel.ch
Homepage: www.zahlenhort-beispiel.ch

```html
<!DOCTYPE html>
<html lang="de">
<head>
<meta charset="utf-8">
<title>zahlenhort-beispiel.ch – Logo &amp; Visitenkarte</title>
<link rel="stylesheet" href="https://fonts.googleapis.com/css2?family=Raleway:wght@400;500;600;700&display=swap">
<style>
  :root {
    --sage-dark: #9aab96;
    --sage-mid: #aabba6;
    --sage-light: #c8d0c1;
    --ochre: #deb37b;
    --card-white: #eff3f6;
    --text-dark: #444a48;
    --text-light: #dde3da;
    --page: #ffffff;
    --band-mid: #e4e1dc;
  }
  * { box-sizing: border-box; margin: 0; padding: 0; }
  html, body { width: 1200px; height: 1200px; overflow: hidden; }
  body {
    position: relative;
    background: var(--page);
    font-family: "Raleway", sans-serif;
  }
  .top-band {
    position: absolute; left: 0; top: 0; width: 1200px; height: 14px;
    background: linear-gradient(to right,
      var(--sage-light) 0 350px, var(--band-mid) 350px 858px, var(--sage-light) 858px);
  }
  .brand {
    position: absolute; left: 0; top: 167px; width: 1200px;
    display: flex; flex-direction: column; align-items: center;
  }
  .brand-square {
    width: 145px; height: 145px; border-radius: 20px;
    background: var(--sage-light);
  }
  .brand-name {
    margin-top: 12px;
    font-size: 46px; font-weight: 600; letter-spacing: 2px; line-height: 1.2;
    color: var(--sage-dark);
  }
  .card {
    position: absolute; left: 345px; width: 519px; height: 296px;
    overflow: hidden;
    box-shadow: 0 6px 18px rgba(0,0,0,0.12);
  }
  .card-front { top: 488px; }
  .card-back { top: 862px; background: var(--card-white); }
  .front-art {
    position: absolute; inset: 0;
    background: linear-gradient(135deg, var(--ochre) 0%, var(--sage-light) 35%, var(--sage-dark) 65%, var(--sage-mid) 100%);
  }
  .front-name {
    position: absolute; left: 0; top: 214px; width: 519px; text-align: center;
    font-size: 38px; font-weight: 700; letter-spacing: 1.5px;
    color: var(--text-light);
  }
  .back-art {
    position: absolute; left: 330px; top: 0; width: 189px; height: 276px;
    background: linear-gradient(160deg, var(--ochre) 0%, var(--sage-light) 40%, var(--sage-dark) 100%);
  }
  .person {
    position: absolute; left: 32px; top: 42px;
  }
  .person-name {
    font-size: 19px; font-weight: 700; letter-spacing: 2px;
    text-transform: uppercase; color: var(--sage-dark);
  }
  .person-title {
    margin-top: 6px;
    font-size: 11.5px; font-weight: 600; letter-spacing: 0.8px; line-height: 1.4;
    text-transform: uppercase; color: var(--text-dark);
  }
  .contact {
    position: absolute; left: 32px; top: 156px;
    font-size: 13.5px; font-weight: 400; letter-spacing: 0.6px; line-height: 19px;
    color: var(--text-dark);
  }
  .contact p + p { margin-top: 18px; }
  .contact .web { color: var(--sage-dark); font-weight: 700; }
</style>
</head>
<body>
  <div class="top-band"></div>

  <header class="brand">
    <div class="brand-square"></div>
    <div class="brand-name">zahlenhort-beispiel.ch</div>
  </header>

  <section class="card card-front" aria-label="Visitenkarte Vorderseite">
    <div class="front-art" role="img" aria-label="Dekorative Farbflächen in Salbeigrün und Ocker"></div>
    <div class="front-name">zahlenhort-beispiel.ch</div>
  </section>

  <section class="card card-back" aria-label="Visitenkarte Rückseite">
    <div class="back-art" role="img" aria-label="Dekorative Farbflächen in Salbeigrün und Ocker"></div>
    <div class="person">
      <h1 class="person-name">Beatrix Vonlanthen</h1>
      <p class="person-title">Fachfrau für Finanz- und<br>Rechnungswesen mit eidg. Fachausweis</p>
    </div>
    <div class="contact">
      <p>Kornacker 17<br>6099 Mattwil</p>
      <p>041 675 42 09<br>beatrix.vonlanthen@zahlenhort-beispiel.ch<br><span class="web">www.zahlenhort-beispiel.ch</span></p>
    </div>
  </section>
</body>
</html>
```